Business Card Design

We just need these details on one side of card and logo on the other.

Industry/Entity Type

Business

Contact Information for Business Card

Lisel Pardoe | Artist
118 Coldwell Street
Malvern East Vic 3145
# 0412 978 205 | 03 9187 2604
lisel@liselpardoe.com
liselsnook.com.au

```html
<!DOCTYPE html>
<html lang="en">
<head>
<meta charset="utf-8">
<title>Pardoe Studio — Business Card</title>
<link rel="stylesheet" href="https://fonts.googleapis.com/css2?family=Open+Sans:wght@400;700&display=swap">
<style>
  :root {
    --stage: #d6d6d6;
    --card-black: #1b1b1b;
    --card-white: #f4f4f4;
    --ink-light: #ffffff;
    --ink-dark: #2a2a2a;
    --ink-muted: #555555;
    --rule: #6a6a6a;
  }
  * { box-sizing: border-box; margin: 0; padding: 0; }
  html, body { width: 1200px; height: 990px; overflow: hidden; }
  body {
    background: var(--stage);
    font-family: "Open Sans", Arial, sans-serif;
    display: flex;
    flex-direction: column;
    align-items: center;
    justify-content: center;
    gap: 40px;
  }
  .card {
    position: relative;
    width: 780px;
    height: 446px;
    background: var(--card-black);
    overflow: hidden;
  }
  .brand {
    position: absolute;
    color: var(--ink-light);
    font-weight: 400;
    line-height: 1;
    letter-spacing: 1px;
    white-space: nowrap;
  }

  /* Front: name side */
  .card-front { background: var(--card-white); padding: 24px; }
  .card-front .inner {
    position: relative;
    width: 100%;
    height: 100%;
    background: var(--card-black);
  }
  .card-front .brand {
    left: 50%;
    top: 50%;
    transform: translate(-50%, -50%);
    font-size: 60px;
  }

  /* Back: details side */
  .card-back .brand { right: 110px; top: 64px; font-size: 50px; }
  .details-panel {
    position: absolute;
    left: 0;
    bottom: 0;
    width: 360px;
    height: 260px;
    background: var(--card-white);
    padding: 26px 34px 0 34px;
    color: var(--ink-dark);
    text-align: right;
  }
  .person-name {
    font-weight: 700;
    font-size: 20px;
    letter-spacing: 1px;
    text-transform: uppercase;
  }
  .person-role {
    font-size: 11px;
    letter-spacing: 2px;
    text-transform: uppercase;
    color: var(--ink-muted);
    margin-bottom: 12px;
  }
  .contact-list { list-style: none; }
  .contact-item {
    display: flex;
    align-items: center;
    justify-content: flex-end;
    gap: 10px;
    font-size: 12px;
    line-height: 1.35;
    padding: 6px 0 5px;
    border-bottom: 1px solid var(--rule);
    margin-left: 40px;
  }
  .contact-item svg { flex: none; width: 12px; height: 12px; fill: var(--ink-dark); }
</style>
</head>
<body>

<section class="card card-front" aria-label="Card front">
  <div class="inner">
    <p class="brand">Pardoe Studio</p>
  </div>
</section>

<section class="card card-back" aria-label="Card back">
  <p class="brand">Pardoe Studio</p>
  <div class="details-panel">
    <p class="person-name">Lisel Pardoe</p>
    <p class="person-role">Artist</p>
    <ul class="contact-list">
      <li class="contact-item">
        <span>0412 978 205 | 03 9187 2604</span>
        <svg viewBox="0 0 24 24" aria-hidden="true"><path d="M6.6 10.8a15.1 15.1 0 0 0 6.6 6.6l2.2-2.2c.3-.3.7-.4 1-.2 1.1.4 2.3.6 3.6.6.6 0 1 .4 1 1V20c0 .6-.4 1-1 1A17 17 0 0 1 3 4c0-.6.4-1 1-1h3.5c.6 0 1 .4 1 1 0 1.3.2 2.5.6 3.6.1.3 0 .7-.2 1z"/></svg>
      </li>
      <li class="contact-item">
        <span>lisel@liselpardoe.com</span>
        <svg viewBox="0 0 24 24" aria-hidden="true"><path d="M2 5h20v14H2z M3.5 6.5 12 13l8.5-6.5" fill="none" stroke="#2a2a2a" stroke-width="2"/></svg>
      </li>
      <li class="contact-item">
        <span>liselsnook.com.au</span>
        <svg viewBox="0 0 24 24" aria-hidden="true"><circle cx="12" cy="12" r="9" fill="none" stroke="#2a2a2a" stroke-width="2"/><path d="M3 12h18M12 3c3 3 3 15 0 18M12 3c-3 3-3 15 0 18" fill="none" stroke="#2a2a2a" stroke-width="1.6"/></svg>
      </li>
      <li class="contact-item">
        <span>118 Coldwell Street<br>Malvern East Vic 3145</span>
        <svg viewBox="0 0 24 24" aria-hidden="true"><path d="M12 2a7 7 0 0 0-7 7c0 5 7 13 7 13s7-8 7-13a7 7 0 0 0-7-7zm0 9.5A2.5 2.5 0 1 1 12 6.5a2.5 2.5 0 0 1 0 5z"/></svg>
      </li>
    </ul>
  </div>
</section>

</body>
</html>
```